Need a tea box packaging design

* Organic Herbal tea
* Imported from india to france for european community
* our main rivals are " DORVE" tea and " BREN" tea.
* the product will be sold online and shops.
* 15 variety of teas will be imported.
* The details in the attached file.
The Packaging contents:
Main page :
Brand Name : SELVO ( logo attached)
Name of the product: KORINE THE VERT ( which means Korine green tea)
Type of the product : Infusion
No of tea bags : 20
Weight of each bag : 1,5 gm
Total weight : 30 gm
Organic label name : Europe ( organic logo attached)
vegan label : vegan ( vegan label attached)
The other side contents will be given later.
A model that i have designed with another designer is attached. It is nice. But i am expecting more than that. ( attached)
Some designs that i like are attached here.
As mentionned earlier there will 15 variety of teas, so the design should easily modifiable by just changing colours.
Project Deadline Extended Reason: I think the deadline is very short due to the weekend. So, I feel it is better to extend the deadline by 5 days. Added Saturday, January 21, 2017
Target Market(s)
Europe. Mainly france.
Industry/Entity Type
Community
Requirements
Must have
- * Design should be modern and colourfull.
- * I like pattern works, Vectorials
- * Yoga silouhaites in the design is appreciable.
- * The design should express wellness, joy and love
Nice to have
- "Dorve" tea in my inspirational design.
- * The ingredients can be showed in vectorial designs in the back ground.
- * The end user must see the box while taking the tea and appreciate
- * The end user must search and find some hidden things.
- * The box must be communicative.
- * Trendy frames.
Should not have
- No need to have tea cups

```html
<!DOCTYPE html>
<html lang="en">
<head>
<meta charset="utf-8">
<title>Selvo – Korine The Vert tea box dieline</title>
<link rel="stylesheet" href="https://fonts.googleapis.com/css2?family=Marcellus+SC&family=Josefin+Sans:wght@300;400&family=Open+Sans:wght@400&display=swap">
<style>
  :root{
    --bg:#bfdcdd;
    --purple-deep:#3f2a84;
    --purple:#5a3b9b;
    --purple-soft:#6a48ad;
    --teal:#18a7b2;
    --yellow:#e7e82c;
    --gold:#d9c56a;
    --leaf:#8ccf3a;
    --cut:#e02c3a;
    --paper:#f4f1ea;
  }
  html,body{margin:0;padding:0;width:1200px;height:954px;overflow:hidden;background:var(--bg);}
  .dieline{display:block;width:1200px;height:954px;}
  .panel-deep{fill:var(--purple-deep);}
  .panel-mid{fill:var(--purple);}
  .frame-teal{fill:var(--teal);}
  .frame-purple{fill:var(--purple);}
  .frame-edge{fill:var(--purple-deep);}
  .cut-line{fill:none;stroke:var(--cut);stroke-width:1.2;}
  .title{font-family:"Marcellus SC",serif;fill:var(--yellow);text-anchor:middle;}
  .flavour{font-family:"Josefin Sans",sans-serif;fill:var(--yellow);text-anchor:middle;font-weight:400;}
  .variety{font-family:"Josefin Sans",sans-serif;fill:var(--gold);text-anchor:middle;font-weight:300;}
  .type{font-family:"Josefin Sans",sans-serif;fill:var(--gold);text-anchor:middle;font-weight:300;letter-spacing:.5px;}
  .brand{font-family:"Josefin Sans",sans-serif;fill:var(--yellow);text-anchor:middle;font-weight:400;letter-spacing:3px;}
  .small-print{font-family:"Open Sans",sans-serif;fill:var(--paper);}
  .organic-badge{fill:var(--leaf);}
  .vegan-badge{fill:var(--paper);}
  .bag-icon{fill:none;stroke:var(--yellow);stroke-width:1.2;}
</style>
</head>
<body>
<svg class="dieline" viewBox="-381.5 0 1500 1193" xmlns="http://www.w3.org/2000/svg" aria-label="Flat dieline of the Selvo Korine The Vert tea box">
  <defs>
    <linearGradient id="pattern-tones" x1="0" y1="0" x2="1" y2="1">
      <stop offset="0" stop-color="#5a3b9b"/>
      <stop offset=".22" stop-color="#2a9db0"/>
      <stop offset=".4" stop-color="#6a48ad"/>
      <stop offset=".58" stop-color="#9fbf3a"/>
      <stop offset=".76" stop-color="#2a9db0"/>
      <stop offset="1" stop-color="#5a3b9b"/>
    </linearGradient>
  </defs>

  <!-- main wrap: side, front, side -->
  <g class="main-wrap">
    <rect class="panel-deep" x="30" y="87" width="677" height="335"/>
    <path role="img" aria-label="Vector pattern of yoga silhouettes and tulsi leaves in purple, teal and yellow"
          fill="url(#pattern-tones)"
          d="M30,87 H707 V198 C610,220 520,280 480,350 V422 H257 V350 C217,280 127,220 30,198 Z"/>
  </g>

  <!-- top flap and front frames -->
  <g class="front-frames">
    <path class="frame-edge" d="M257,40 H480 L368,218 Z"/>
    <path class="frame-teal" d="M264,40 H473 L368,205 Z"/>
    <path class="frame-edge" d="M368,196 L480,422 H257 Z"/>
    <path class="frame-purple" d="M368,212 L466,422 H271 Z"/>
  </g>

  <!-- front text -->
  <g class="front-label">
    <text class="variety" x="368" y="113" font-size="13">Korine</text>
    <text class="flavour" x="368" y="131" font-size="17">Lemon Mint</text>
    <text class="type" x="368" y="149" font-size="13">INFUSION</text>
    <path class="bag-icon" d="M360,160 h16 v24 h-16 z M366,160 l2,-4 l2,4 M376,172 c4,2 4,8 4,14"/>
    <text class="flavour" x="368" y="178" font-size="10">20</text>

    <text class="title" x="368" y="304" font-size="25">Korine</text>
    <text class="title" x="368" y="333" font-size="25">The Vert</text>
    <circle cx="313" cy="356" r="4" fill="var(--yellow)"/>
    <text class="brand" x="372" y="363" font-size="18">SELVO</text>

    <rect class="organic-badge" x="273" y="385" width="42" height="27"/>
    <text class="small-print" x="337" y="396" font-size="6.5">net weight 1,5gm</text>
    <text class="small-print" x="337" y="406" font-size="6.5">total weight 30gm</text>
    <circle class="vegan-badge" cx="440" cy="398" r="15"/>
  </g>

  <!-- bottom panel -->
  <g class="base-panel">
    <rect class="panel-mid" x="171" y="422" width="395" height="189"/>
    <rect role="img" aria-label="Yoga figure and leaf emblem" x="328" y="438" width="80" height="66" rx="22" fill="url(#pattern-tones)"/>
    <circle cx="292" cy="540" r="6" fill="var(--yellow)"/>
    <text class="brand" x="374" y="551" font-size="30">SELVO</text>
    <text class="small-print" x="282" y="583" font-size="7">Batch no.</text>
    <text class="small-print" x="282" y="594" font-size="7">Best before</text>
  </g>

  <!-- back panel -->
  <g class="back-panel">
    <rect class="panel-deep" x="257" y="611" width="223" height="337"/>
    <g transform="rotate(180 368 660)">
      <circle cx="302" cy="652" r="5" fill="var(--yellow)"/>
      <text class="brand" x="374" y="669" font-size="26">SELVO</text>
    </g>
    <path role="img" aria-label="Vector pattern of yoga silhouettes and tulsi leaves"
          fill="url(#pattern-tones)" d="M257,850 Q368,822 480,850 V948 H257 Z"/>
    <g transform="rotate(180 368 900)">
      <text class="title" x="368" y="900" font-size="19">Korine The Vert</text>
      <text class="flavour" x="368" y="918" font-size="11">Korine Lemon Mint INFUSION</text>
    </g>
  </g>

  <!-- lower tuck panel -->
  <g class="tuck-panel">
    <rect role="img" aria-label="Vector pattern of yoga silhouettes and tulsi leaves"
          x="171" y="948" width="395" height="190" fill="url(#pattern-tones)"/>
    <path class="frame-edge" d="M368,938 L480,1138 H257 Z"/>
    <path class="frame-teal" d="M368,956 L466,1138 H271 Z"/>
    <text class="title" x="368" y="1060" font-size="18">Korine</text>
    <text class="title" x="368" y="1079" font-size="19">The Vert</text>
    <text class="type" x="368" y="1093" font-size="11">INFUSION</text>
    <circle cx="318" cy="1107" r="4" fill="var(--yellow)"/>
    <text class="brand" x="372" y="1114" font-size="17">SELVO</text>
  </g>

  <!-- cut and fold lines -->
  <g class="cut-guides">
    <path class="cut-line" d="M257,87 V40 H480 V87"/>
    <rect class="cut-line" x="30" y="87" width="677" height="335"/>
    <line class="cut-line" x1="70" y1="87" x2="70" y2="422"/>
    <line class="cut-line" x1="257" y1="87" x2="257" y2="422"/>
    <line class="cut-line" x1="480" y1="87" x2="480" y2="422"/>
    <line class="cut-line" x1="667" y1="87" x2="667" y2="422"/>
    <rect class="cut-line" x="171" y="422" width="395" height="189"/>
    <line class="cut-line" x1="257" y1="422" x2="257" y2="611"/>
    <line class="cut-line" x1="480" y1="422" x2="480" y2="611"/>
    <rect class="cut-line" x="257" y="611" width="223" height="337"/>
    <rect class="cut-line" x="171" y="948" width="395" height="190"/>
    <line class="cut-line" x1="257" y1="948" x2="257" y2="1138"/>
    <line class="cut-line" x1="480" y1="948" x2="480" y2="1138"/>
  </g>
</svg>
</body>
</html>
```